Flyer / Mailer for Business Debt Relief Business - Harborline Relief 6" x 11"

We need a 6" x 11" double sided flyer. This will be sent out to potential customers with high interest business loans. We would like the design to coordinate with the colors of our logo. I have included a mock up that we sketched out. I have also included a file of a mailer we received that we would like to use as a template (not colors or fonts, just set up). I have also included an .ai file of our logo.

```html
<!DOCTYPE html>
<html lang="en">
<head>
<meta charset="utf-8">
<title>Harborline Relief – Business Debt Relief Mailer</title>
<link href="https://fonts.googleapis.com/css2?family=Montserrat:wght@400;500;600;700&family=Source+Serif+4:ital,wght@1,400;1,600;1,700&display=swap" rel="stylesheet">
<style>
  :root {
    --page-bg: #ececec;
    --card-white: #ffffff;
    --brand-green: #3a8f2f;
    --tick-green: #4cae3a;
    --link-green: #6cc24a;
    --brand-blue: #1f5f99;
    --deep-blue: #0a4f8c;
    --navy: #0e1f3d;
    --tagline-blue: #4a78a8;
    --ink-grey: #555b63;
    --sans: "Montserrat", Arial, sans-serif;
    --serif: "Source Serif 4", Georgia, serif;
  }
  * { box-sizing: border-box; margin: 0; padding: 0; }
  html, body { width: 1200px; height: 788px; overflow: hidden; }
  body { background: var(--page-bg); position: relative; font-family: var(--sans); }

  .card { position: absolute; left: 270px; width: 660px; height: 360px; overflow: hidden; background: var(--card-white); }
  .card--front { top: 20px; }
  .card--back { top: 408px; }

  /* Front: photo column */
  .photo-column { position: absolute; left: 0; top: 0; width: 133px; height: 360px; display: flex; flex-direction: column; }
  .photo-tile { flex: 1; }
  .photo-tile--couple { background: linear-gradient(135deg, #8a7a6a, #d9d2c8); }
  .photo-tile--savings { background: linear-gradient(135deg, #b98672, #efc9bd); }
  .photo-tile--paperwork { background: linear-gradient(135deg, #3a4150, #d8dbe0); }
  .photo-tile--chart { background: linear-gradient(135deg, #2a3a8c, #7a5fc4 55%, #3d8fd6); }

  /* Front: main panel */
  .front-main { position: absolute; left: 133px; top: 0; width: 527px; height: 360px; }
  .front-header { height: 50px; display: flex; align-items: center; justify-content: space-between; padding: 0 20px 0 21px; }
  .tagline { font-family: var(--serif); font-style: italic; font-size: 15.5px; color: var(--tagline-blue); }
  .brand-name { display: flex; align-items: center; gap: 5px; font-family: var(--sans); font-weight: 600; font-size: 8px; letter-spacing: 0.8px; color: var(--brand-blue); text-transform: uppercase; }
  .brand-mark { width: 12px; height: 12px; background: var(--brand-green); }

  .headline-band { position: relative; z-index: 1; height: 50px; background: var(--brand-green); padding: 7px 21px; }
  .headline { color: #fff; font-weight: 700; font-size: 13.2px; line-height: 17px; max-width: 380px; }

  .offer-panel { position: relative; height: 180px; background: var(--navy); }
  .offer-photo { position: absolute; right: 0; top: 0; width: 330px; height: 180px;
    background: linear-gradient(90deg, rgba(14,31,61,1) 0%, rgba(40,62,100,0.9) 25%, #52698e 55%, #8fa6c4 80%, #6f86a8 100%); }
  .offer-copy { position: relative; padding: 10px 21px 0; color: #fff; }
  .offer-title { font-weight: 700; font-size: 10.2px; letter-spacing: 0.2px; }
  .offer-sub { font-family: var(--serif); font-style: italic; font-weight: 700; font-size: 11px; margin-bottom: 6px; }
  .benefit-list { list-style: none; }
  .benefit { display: flex; align-items: center; gap: 5px; font-size: 8.6px; line-height: 13.1px; }
  .benefit svg { flex: none; }

  .contact-band { height: 80px; background: var(--deep-blue); text-align: center; color: #fff; padding-top: 11px; }
  .cta { font-family: var(--serif); font-style: italic; font-weight: 700; font-size: 12.8px; margin-bottom: 3px; }
  .contact-line { display: flex; justify-content: center; align-items: center; gap: 6px; font-weight: 700; font-size: 10px; line-height: 14px; }
  .website { margin-top: 6px; font-size: 6.6px; font-weight: 600; letter-spacing: 0.3px; color: var(--link-green); text-transform: uppercase; }

  /* Back */
  .return-block { position: absolute; left: 8px; top: 14px; width: 140px; text-align: center; }
  .return-mark { width: 26px; height: 26px; background: var(--brand-green); margin: 0 auto 7px; }
  .return-name { font-weight: 500; font-size: 9.5px; letter-spacing: 1px; color: var(--ink-grey); text-transform: uppercase; white-space: nowrap; }
  .return-address { margin-top: 8px; font-size: 6px; font-weight: 700; line-height: 7.5px; color: var(--ink-grey); text-transform: uppercase; }
  .back-message { position: absolute; left: 24px; top: 122px; width: 180px; }
  .back-heading { font-weight: 500; font-size: 10px; line-height: 12px; color: var(--deep-blue); text-transform: uppercase; margin-bottom: 7px; }
  .back-copy { font-family: var(--serif); font-style: italic; font-size: 8.6px; line-height: 13.5px; color: var(--deep-blue); }
</style>
</head>
<body>

<section class="card card--front">
  <div class="photo-column">
    <div class="photo-tile photo-tile--couple" role="img" aria-label="Photo of a couple reviewing bills at home"></div>
    <div class="photo-tile photo-tile--savings" role="img" aria-label="Photo of a hand dropping a coin into a pink piggy bank"></div>
    <div class="photo-tile photo-tile--paperwork" role="img" aria-label="Photo of hands reviewing financial documents with a pen"></div>
    <div class="photo-tile photo-tile--chart" role="img" aria-label="Photo of a glowing financial chart on a screen"></div>
  </div>

  <div class="front-main">
    <header class="front-header">
      <p class="tagline">Helping Businesses Focus On What Matters!</p>
      <p class="brand-name"><span class="brand-mark"></span>Harborline Relief</p>
    </header>

    <div class="headline-band">
      <h1 class="headline">We understand that merchant cash advance loans can be a burden on your business</h1>
    </div>

    <div class="offer-panel">
      <div class="offer-photo" role="img" aria-label="Photo of business professionals reviewing documents in a bright office"></div>
      <div class="offer-copy">
        <h2 class="offer-title">OVERWHELMED BY DAILY/WEEKLY PAYMENTS?</h2>
        <p class="offer-sub">We Can Help!</p>
        <ul class="benefit-list">
          <li class="benefit"><svg width="9" height="9" viewBox="0 0 10 10"><circle cx="5" cy="5" r="5" fill="#4cae3a"/><path d="M2.6 5.1l1.6 1.6 3.2-3.3" stroke="#fff" stroke-width="1.4" fill="none"/></svg>This is not a loan, WE ARE NOT LENDERS!</li>
          <li class="benefit"><svg width="9" height="9" viewBox="0 0 10 10"><circle cx="5" cy="5" r="5" fill="#4cae3a"/><path d="M2.6 5.1l1.6 1.6 3.2-3.3" stroke="#fff" stroke-width="1.4" fill="none"/></svg>Improve your business's cash flow immediately</li>
          <li class="benefit"><svg width="9" height="9" viewBox="0 0 10 10"><circle cx="5" cy="5" r="5" fill="#4cae3a"/><path d="M2.6 5.1l1.6 1.6 3.2-3.3" stroke="#fff" stroke-width="1.4" fill="none"/></svg>Move payments to one monthly amount</li>
          <li class="benefit"><svg width="9" height="9" viewBox="0 0 10 10"><circle cx="5" cy="5" r="5" fill="#4cae3a"/><path d="M2.6 5.1l1.6 1.6 3.2-3.3" stroke="#fff" stroke-width="1.4" fill="none"/></svg>Reduce the amount you are paying out monthly</li>
          <li class="benefit"><svg width="9" height="9" viewBox="0 0 10 10"><circle cx="5" cy="5" r="5" fill="#4cae3a"/><path d="M2.6 5.1l1.6 1.6 3.2-3.3" stroke="#fff" stroke-width="1.4" fill="none"/></svg>Strategic alternatives to high interest loans</li>
          <li class="benefit"><svg width="9" height="9" viewBox="0 0 10 10"><circle cx="5" cy="5" r="5" fill="#4cae3a"/><path d="M2.6 5.1l1.6 1.6 3.2-3.3" stroke="#fff" stroke-width="1.4" fill="none"/></svg>Fast, confidential business debt relief</li>
          <li class="benefit"><svg width="9" height="9" viewBox="0 0 10 10"><circle cx="5" cy="5" r="5" fill="#4cae3a"/><path d="M2.6 5.1l1.6 1.6 3.2-3.3" stroke="#fff" stroke-width="1.4" fill="none"/></svg>No-obligation consultation</li>
          <li class="benefit"><svg width="9" height="9" viewBox="0 0 10 10"><circle cx="5" cy="5" r="5" fill="#4cae3a"/><path d="M2.6 5.1l1.6 1.6 3.2-3.3" stroke="#fff" stroke-width="1.4" fill="none"/></svg>Absolutely no credit pulls</li>
          <li class="benefit"><svg width="9" height="9" viewBox="0 0 10 10"><circle cx="5" cy="5" r="5" fill="#4cae3a"/><path d="M2.6 5.1l1.6 1.6 3.2-3.3" stroke="#fff" stroke-width="1.4" fill="none"/></svg>No collateral, no financials</li>
        </ul>
      </div>
    </div>

    <footer class="contact-band">
      <p class="cta">Call Now For Free Consultation With Our Experts</p>
      <p class="contact-line"><svg width="10" height="8" viewBox="0 0 10 8"><rect width="10" height="8" rx="1" fill="#4cae3a"/><path d="M0.5 1l4.5 3.3L9.5 1" stroke="#0a4f8c" stroke-width="1" fill="none"/></svg>800-555-0142</p>
      <p class="contact-line"><svg width="9" height="9" viewBox="0 0 10 10"><path d="M2.2 0.6l1.6 2.2-1 1.1c.6 1.3 1.7 2.4 3 3l1.1-1 2.2 1.6-.7 1.7C5.6 9.4.6 4.4.5 1.3z" fill="#4cae3a"/></svg>info@harborlinerelief.com</p>
      <p class="website">Visit our website: harborlinerelief.com</p>
    </footer>
  </div>
</section>

<section class="card card--back">
  <div class="return-block">
    <div class="return-mark"></div>
    <p class="return-name">Harborline Relief</p>
    <p class="return-address">1480 Meridian Ave<br>Fairview, TX 75010</p>
  </div>
  <div class="back-message">
    <h2 class="back-heading">Strategic debt relief for<br>businesses of all sizes</h2>
    <p class="back-copy">Stop taking out loans to pay off other loans.<br>Take back your business's cash flow, and<br>focus on what matters</p>
  </div>
</section>

</body>
</html>
```